Civil engineering company | Billboard

We need a billboard design for Velmora- civil engineering company. We want big logo in the center of billboard and web site (www.velmora.hr) below the logo. Also, we want an subtle abstract pattern in the background. Dimensions of the billboard are: width :10 m, height: 2m. Design must be celan and modern.
Industry/Entity Type
Civil engineering
Font styles to use
Sans Serif
Colors
F0912C
F2A743
F7CA91
FBE8D2
FDF5EE
Requirements
Must have
- Logo and new unique pattern design for Velmroa company
Should not have
- pictures of construction machinery and tools

```html
<!DOCTYPE html>
<html lang="hr">
<head>
<meta charset="utf-8">
<title>Velmora – billboard</title>
<link href="https://fonts.googleapis.com/css2?family=Montserrat:wght@500;600;700&display=swap" rel="stylesheet">
<style>
  :root {
    --stage: #ececec;
    --paper: #ffffff;
    --charcoal: #2b2b2a;
    --orange: #e9923a;
    --steel: #6f6f6f;
    --tagline: #5a5a5a;
  }
  html, body {
    margin: 0;
    padding: 0;
    width: 1200px;
    height: 420px;
    overflow: hidden;
    background: var(--stage);
  }
  .billboard {
    position: absolute;
    left: 0;
    top: 90px;
    width: 1200px;
    height: 240px;
    background: var(--paper);
    overflow: hidden;
    font-family: "Montserrat", sans-serif;
  }
  .billboard-shapes {
    position: absolute;
    inset: 0;
    width: 1200px;
    height: 240px;
  }
  .pattern-field { fill: var(--charcoal); }
  .accent-orange { fill: var(--orange); }
  .accent-dark { fill: var(--charcoal); }
  .brand-block {
    position: absolute;
    left: 430px;
    top: 37px;
    width: 336px;
    text-align: center;
  }
  .brand-square {
    width: 70px;
    height: 82px;
    margin: 0 auto;
    border: 3px solid var(--steel);
    box-sizing: border-box;
  }
  .brand-name {
    margin: 36px 0 0;
    font-size: 44px;
    line-height: 1;
    font-weight: 500;
    letter-spacing: 3px;
    color: var(--orange);
    text-transform: uppercase;
  }
  .brand-tagline {
    margin: 8px 0 0;
    font-size: 10.5px;
    font-weight: 700;
    letter-spacing: 0.2px;
    color: var(--tagline);
    text-transform: uppercase;
    white-space: nowrap;
  }
  .web-bar {
    position: absolute;
    left: 807px;
    top: 172px;
    width: 393px;
    height: 39px;
    background: var(--charcoal);
  }
  .web-address {
    position: absolute;
    left: 45px;
    top: 0;
    line-height: 39px;
    margin: 0;
    font-size: 25px;
    font-weight: 500;
    letter-spacing: 1px;
    color: var(--paper);
    text-transform: uppercase;
  }
</style>
</head>
<body>
  <main class="billboard">
    <svg class="billboard-shapes" viewBox="0 0 1200 240" aria-hidden="false">
      <polygon class="pattern-field" role="img" aria-label="Subtle abstract geometric pattern in charcoal and muted orange" points="0,0 416,0 241,240 0,240"/>
      <polygon class="accent-orange" points="344,99 359,99 255,240 241,240"/>
      <polygon class="accent-dark" points="938,0 956,0 856,139 843,139"/>
      <polygon class="accent-orange" points="956,0 1200,0 1200,240 784,240"/>
    </svg>

    <section class="brand-block">
      <div class="brand-square"></div>
      <h1 class="brand-name">Velmora</h1>
      <p class="brand-tagline">Izvođenje i vođenje građevinskih radova</p>
    </section>

    <div class="web-bar">
      <p class="web-address">www.velmora.hr</p>
    </div>
  </main>
</body>
</html>
```